Under Copper Lanterns to WANDERLAND - Practical notes on Arranging your garden, kitchen, and study.

PLEASE READ: My book is all about optimizing a person's health.
Most people go through life in pain, low energy, disappointed with their body and living a short life relying on medication. I call this "Surviving"

My Goal is to transform their life from serving to THRIVING. This is why you see the background I these images as a cold, dark cracking desert. From this cold dark desert I want there to be a thriving and emerging plant brain like the one seen on image #1. I also want my readers to pick up the book and know that the book is about humans. So I want there to be a nervous system like in image #2 Lastly on image 3. I want there to be consistency throughout the whole book. Like the cracking desert in the background of the back cover.

Target Market(s)

People struggling with their health

Industry/Entity Type

Health

Colors
0054AA
0677BA
7BADD7
CADEEF
E8F1F8
00AB8E
00BBA5
67D7C9
C6EFE9
E9F9F6

Requirements
Must have
• Brain, and Nervous system.
Nice to have
• Colors selected

```html
<!DOCTYPE html>
<html lang="en">
<head>
<meta charset="utf-8">
<title>Under Copper Lanterns to Wanderland — Book Cover</title>
<link rel="stylesheet" href="https://fonts.googleapis.com/css2?family=Bebas+Neue&family=Montserrat:wght@400;500&display=swap">
<style>
  :root {
    --stage: #262626;
    --paper: #ffffff;
    --blue-light: #7badd7;
    --blue-deep: #0677ba;
    --band: #0872b8;
    --ink: #111111;
    --ground-grey: #d9d9d9;
    --leaf-green: #6cbf3a;
  }
  html, body {
    margin: 0;
    padding: 0;
    width: 1200px;
    height: 800px;
    overflow: hidden;
    background: var(--stage);
  }
  .canvas {
    width: 1200px;
    height: 800px;
    display: flex;
    align-items: center;
    justify-content: center;
  }
  .book-cover {
    width: 510px;
    height: 762px;
    display: block;
    background: var(--paper);
  }
  .title-small {
    font-family: "Montserrat", sans-serif;
    font-weight: 500;
    fill: var(--blue-light);
  }
  .title-upper {
    font-family: "Bebas Neue", sans-serif;
    fill: var(--blue-light);
  }
  .title-main {
    font-family: "Bebas Neue", sans-serif;
    fill: var(--blue-deep);
  }
  .rule { stroke: var(--blue-light); stroke-width: 2; }
  .subtitle {
    font-family: "Montserrat", sans-serif;
    font-weight: 400;
    font-size: 14.5px;
    fill: var(--ink);
  }
  .author-band { fill: var(--band); }
  .author-name {
    font-family: "Montserrat", sans-serif;
    font-weight: 400;
    font-size: 22px;
    letter-spacing: 3px;
    fill: var(--paper);
  }
</style>
</head>
<body>
<main class="canvas">
  <svg class="book-cover" viewBox="0 0 510 762" xmlns="http://www.w3.org/2000/svg">
    <defs>
      <radialGradient id="groundGlow" cx="50%" cy="72%" r="55%">
        <stop offset="0%" stop-color="#8a8f86"/>
        <stop offset="35%" stop-color="var(--ground-grey)"/>
        <stop offset="100%" stop-color="#ffffff" stop-opacity="0"/>
      </radialGradient>
      <radialGradient id="sproutGlow" cx="50%" cy="22%" r="22%">
        <stop offset="0%" stop-color="var(--leaf-green)" stop-opacity="0.75"/>
        <stop offset="100%" stop-color="var(--leaf-green)" stop-opacity="0"/>
      </radialGradient>
    </defs>

    <rect width="510" height="762" fill="var(--paper)"/>

    <g class="title-block">
      <line class="rule" x1="33" y1="65" x2="190" y2="65"/>
      <line class="rule" x1="320" y1="65" x2="477" y2="65"/>
      <text class="title-small" x="255" y="75" text-anchor="middle" font-size="26" textLength="120" lengthAdjust="spacingAndGlyphs">UNDER COPPER</text>

      <text class="title-upper" x="33" y="182" font-size="134" textLength="444" lengthAdjust="spacingAndGlyphs">LANTERNS</text>

      <line class="rule" x1="33" y1="205" x2="233" y2="205"/>
      <line class="rule" x1="277" y1="205" x2="477" y2="205"/>
      <text class="title-small" x="255" y="214" text-anchor="middle" font-size="24" textLength="32" lengthAdjust="spacingAndGlyphs">TO</text>

      <text class="title-main" x="33" y="341" font-size="168" textLength="444" lengthAdjust="spacingAndGlyphs">WANDERLAND</text>
    </g>

    <g class="cover-artwork" role="img" aria-label="Illustration: a green seedling sprouting from cracked grey dry ground">
      <rect x="62" y="378" width="398" height="225" fill="url(#groundGlow)"/>
      <rect x="62" y="378" width="398" height="225" fill="url(#sproutGlow)"/>
    </g>

    <text class="subtitle" x="255" y="640" text-anchor="middle">Practical notes on Arranging your</text>
    <text class="subtitle" x="255" y="660" text-anchor="middle">garden, kitchen, and study</text>

    <rect class="author-band" x="0" y="719" width="510" height="43"/>
    <text class="author-name" x="255" y="748" text-anchor="middle">AUTHOR NAME</text>
  </svg>
</main>
</body>
</html>
```